Label Design For Vitamin C Serum for Larkwind Skin Care

I need a label design for a bottle similar to this:

https://www.tradelumo-market.example/item/Sample-Face-Serum-Bottle/50000000001.html

Industry/Entity Type

Skin Care Product

Font styles to use
Other font styles liked:
• use logo and use anything standard for label text

Colors
000000

Requirements
Must have
• 20% Vitamin C Brightening Serum
• 30 ML
• On back of label:
• Vitamin C serum is a potent antioxidant designed to help minimize the damaging effects of free oxygen radicals.
• This formulation will help restore skin tone and youthful appearance to the skin.
• Apply 2-3 drops of serum to desired areas. Massage with fingertips.
Nice to have
• I want to use the GOLD LOGO with BLACK LABEL

```html
<!DOCTYPE html>
<html lang="en">
<head>
<meta charset="utf-8">
<title>Larkwind Skin Care – Vitamin C Serum Labels</title>
<link href="https://fonts.googleapis.com/css2?family=Open+Sans:wght@400;600&display=swap" rel="stylesheet">
<style>
  :root {
    --canvas-bg: #ffffff;
    --label-black: #000000;
    --gold: #c9a04a;
    --gold-light: #f2d588;
    --gold-dark: #a97c2c;
    --text-light: #ffffff;
    --text-dark: #2a2115;
  }
  * { box-sizing: border-box; margin: 0; padding: 0; }
  html, body {
    width: 1200px;
    height: 1044px;
    overflow: hidden;
    background: var(--canvas-bg);
  }
  .canvas {
    position: relative;
    width: 1200px;
    height: 1044px;
  }
  .label {
    position: absolute;
    top: 390px;
    width: 290px;
    height: 400px;
    background: var(--label-black);
    font-family: "Open Sans", Arial, sans-serif;
    color: var(--text-light);
    text-align: center;
  }
  .label--front { left: 218px; }
  .label--back  { left: 533px; }
  .label__band {
    position: absolute;
    left: 0;
    width: 100%;
    height: 6px;
    background: linear-gradient(90deg, var(--gold-dark), var(--gold-light) 50%, var(--gold-dark));
  }
  .label__band--top { top: 14px; }
  .label__band--bottom { bottom: 14px; }

  .brand {
    position: absolute;
    top: 92px;
    left: 0;
    width: 100%;
    font-size: 20px;
    font-weight: 600;
    letter-spacing: 1px;
    color: var(--gold);
  }
  .product-strength {
    position: absolute;
    top: 192px;
    left: 0;
    width: 100%;
    font-size: 20px;
    font-weight: 400;
  }
  .product-type {
    position: absolute;
    top: 244px;
    left: 24px;
    width: 242px;
    height: 32px;
    line-height: 32px;
    font-size: 15px;
    color: var(--text-dark);
    background: linear-gradient(90deg, var(--gold-dark), var(--gold-light) 50%, var(--gold-dark));
  }
  .volume {
    position: absolute;
    bottom: 52px;
    left: 0;
    width: 100%;
    font-size: 13px;
  }

  .back-copy {
    position: absolute;
    top: 68px;
    left: 34px;
    width: 222px;
    font-size: 13px;
    line-height: 1.3;
  }
  .back-copy p + p { margin-top: 16px; }
</style>
</head>
<body>
<main class="canvas">
  <section class="label label--front">
    <div class="label__band label__band--top"></div>
    <h1 class="brand">Larkwind Skin Care</h1>
    <p class="product-strength">20% Vitamin C</p>
    <p class="product-type">Brightening Serum</p>
    <p class="volume">30 ml</p>
    <div class="label__band label__band--bottom"></div>
  </section>

  <section class="label label--back">
    <div class="label__band label__band--top"></div>
    <div class="back-copy">
      <p>Vitamin C serum is a potent antioxidant designed to help minimize the damaging effects of free oxygen radicals.</p>
      <p>This formulation will help restore skin tone and youthful appearance to the skin.</p>
      <p>Apply 2-3 drops of serum to desired areas. Massage with fingertips.</p>
    </div>
    <div class="label__band label__band--bottom"></div>
  </section>
</main>
</body>
</html>
```